Book Cover Design for Millennial

I need a book cover design for my book Sunward Ledger. The subtitle of the book is Seven Quiet Steps Toward Steady Ground at Work.

I'm a career coach who helps millennial career professionals. I myself am a millennial but on the older end (34). I've dealt and been through most of the challenges millennials are facing as career professionals and I wrote this book with the thought of providing guidance and aid to getting past those challenges and shedding light on fundamental habits and practices that will help them excel in their careers. In addition, the book will help them prepare millennials for our turn as the leaders, managers, etc moving forward in corporate America. The final design should have the main title of the book in it as the focal point but not the subtitle. I want the cover to communicate something NEW, Bold, Youthful, non-traditional. I want it to stick out while still maintaining a sleek and Professional look.
Updates

Hello, Designers! I want to thank you all for your submissions! The work is amazing and I greatly appreciate it. If you would I want to help out in this process by adding a few updates based on the submissions I have seen. The concept I think that is coming close to hitting the mark is Bramble Forja. What I would like to see changed about the concept is the following: Change the outfits to be more Millennial Career Professional. I have attached some ideas to the brief. I want to replace this picture with one of multiple millennials anywhere from 3 and up. I would like the pic to have diversity in it representing most races of people in the USA. I would like my name beneath sunward ledger. I'm not a known author yet so having my name that big my distract from the title of the book. Can we make the title a little bigger and so far I like the background.Thanks, DP Added Friday, September 30, 2016

Target Market(s)

Millennial Career Professionals (18 - 34 age group)

Industry/Entity Type

Life Coaching

Logo Text

Sunward Ledger

Requirements
Must have
• communicate something NEW, Bold, Youthful, non-traditional. I want it to stick out while still maintaining a sleek and Professional look.
Nice to have
• something that goes with my brand
• http://www.doranpelwick.com
Should not have
• Nothing 3D or a logo that is hard to read when placed on stationeries, business cards etc

```html
<!DOCTYPE html>
<html lang="en">
<head>
<meta charset="utf-8">
<title>Sunward Ledger — Book Cover</title>
<link href="https://fonts.googleapis.com/css2?family=Anton&family=Montserrat:wght@300;400;600&family=Passion+One:wght@700&display=swap" rel="stylesheet">
<style>
  :root {
    --back-top: #1c63cf;
    --back-bottom: #0a3696;
    --spine: #0c3a8c;
    --title-blue: #1fa9f2;
    --white: #ffffff;
    --box-fill: #0c3b8f;
    --box-line: #3d6fc4;
    --dark-block: #061a4a;
    --front-dark: #2a3848;
    --front-mid: #6f8db0;
    --front-light: #c6d6e6;
    --author-navy: #15285a;
  }
  * { margin: 0; padding: 0; box-sizing: border-box; }
  html, body { width: 1200px; height: 902px; overflow: hidden; background: #fff; }
  .cover-wrap { position: relative; width: 1200px; height: 902px; }

  .back-cover {
    position: absolute; left: 0; top: 0; width: 584px; height: 902px;
    background: linear-gradient(180deg, var(--back-top) 0%, #1450b8 45%, var(--back-bottom) 100%);
    color: var(--white);
    font-family: 'Montserrat', sans-serif;
  }
  .back-heading { position: absolute; left: 0; top: 0; }
  .back-blurb {
    position: absolute; left: 48px; top: 127px; width: 488px;
    font-size: 13.6px; line-height: 17.7px; text-align: justify; font-weight: 400;
  }
  .author-photo-slot {
    position: absolute; left: 47px; top: 451px; width: 163px; height: 188px;
    background: var(--box-fill); border: 1px solid var(--box-line);
  }
  .about-heading {
    position: absolute; left: 243px; top: 450px;
    font-size: 13.6px; font-weight: 600; letter-spacing: 0.2px;
  }
  .about-text {
    position: absolute; left: 243px; top: 476px; width: 305px;
    font-size: 13.6px; line-height: 17.7px; text-align: justify;
  }
  .barcode-area {
    position: absolute; left: 50px; top: 808px; width: 111px; height: 62px;
    background: var(--dark-block);
  }

  .spine {
    position: absolute; left: 584px; top: 0; width: 32px; height: 902px;
    background: var(--spine);
  }
  .spine svg { position: absolute; left: 0; top: 0; }

  .front-cover {
    position: absolute; left: 616px; top: 0; width: 584px; height: 902px; overflow: hidden;
    background:
      radial-gradient(ellipse 70% 22% at 50% 36%, var(--front-light) 0%, rgba(198,214,230,0) 70%),
      linear-gradient(180deg, var(--front-dark) 0%, #3d4f63 22%, var(--front-mid) 42%, #8aa6c6 70%, #5e86b8 100%);
  }
  .front-cover svg.front-type { position: absolute; left: 0; top: 0; }
  .group-photo {
    position: absolute; left: 16px; top: 380px; width: 568px; height: 410px;
    border-radius: 120px 120px 0 0;
    background: linear-gradient(180deg, #55606e 0%, #3b3f47 40%, #2e323a 70%, rgba(110,140,175,0) 100%);
  }
</style>
</head>
<body>
<div class="cover-wrap">

  <section class="back-cover">
    <svg class="back-heading" width="584" height="120" viewBox="0 0 584 120">
      <text x="52" y="88" fill="#1fa9f2" font-family="'Passion One', sans-serif" font-weight="700" font-size="56" textLength="492" lengthAdjust="spacingAndGlyphs">SUNWARD LEDGER</text>
      <text x="152" y="109" fill="#1fa9f2" font-family="'Passion One', sans-serif" font-weight="700" font-size="14" textLength="328" lengthAdjust="spacingAndGlyphs">SEVEN QUIET STEPS TOWARD STEADY GROUND AT WORK.</text>
    </svg>
    <p class="back-blurb">Lorem Ipsum is simply dummy text of the printing and typesetting industry. Lorem Ipsum has been the industry's standard dummy text ever since the 1500s, when an unknown printer took a galley of type and scrambled it to make a type specimen book. It has survived not only five centuries, but also the leap into electronic typesetting, remaining essentially unchanged. It was popularised in the 1960s with the release of Typeleaf sheets containing Lorem Ipsum passages, and more recently with desktop publishing software like Quillset Layout including versions of Lorem Ipsum. Lorem Ipsum is simply dummy text of the printing and typesetting industry. Lorem Ipsum has been the industry's standard dummy text ever since the 1500s, when an unknown printer took a galley of type and scrambled it to make a type specimen book. It has survived not only five centuries, but also the leap into electronic typesetting, remaining essentially</p>
    <div class="author-photo-slot" role="img" aria-label="Author portrait placeholder"></div>
    <h3 class="about-heading">ABOUT AUTHOR</h3>
    <p class="about-text">Lorem Ipsum is simply dummy text of the printing and typesetting industry. Lorem Ipsum has been the industry's standard dummy text ever since the 1500s, when an unknown printer took a galley of type and scrambled it to make a type specimen book. It has survived not only five centuries, but also the leap into electronic typesetting, remaining essentially</p>
    <div class="barcode-area"></div>
  </section>

  <section class="spine">
    <svg width="32" height="902" viewBox="0 0 32 902">
      <g fill="#ffffff" font-family="Montserrat, sans-serif" font-weight="300" font-size="25">
        <text transform="translate(7,52) rotate(90)" textLength="392" lengthAdjust="spacingAndGlyphs">SUNWARD LEDGER</text>
        <text transform="translate(7,598) rotate(90)" textLength="270" lengthAdjust="spacingAndGlyphs">DORAN PELWICK</text>
      </g>
    </svg>
  </section>

  <section class="front-cover">
    <div class="group-photo" role="img" aria-label="Group photo of ten diverse young professionals in business attire"></div>
    <svg class="front-type" width="584" height="902" viewBox="0 0 584 902">
      <defs>
        <linearGradient id="titleGold" x1="0" y1="0" x2="1" y2="1">
          <stop offset="0" stop-color="#ffe600"/>
          <stop offset="0.45" stop-color="#ffc400"/>
          <stop offset="0.55" stop-color="#f2a200"/>
          <stop offset="1" stop-color="#ffb300"/>
        </linearGradient>
      </defs>
      <g font-family="Anton, sans-serif" fill="url(#titleGold)" font-size="112">
        <text x="40" y="136" textLength="504" lengthAdjust="spacingAndGlyphs">SUNWARD</text>
        <text x="40" y="262" textLength="504" lengthAdjust="spacingAndGlyphs">LEDGER</text>
      </g>
      <text x="42" y="299" fill="#ffffff" font-family="'Passion One', sans-serif" font-weight="700" font-size="22" textLength="500" lengthAdjust="spacingAndGlyphs">SEVEN QUIET STEPS TOWARD STEADY GROUND AT WORK.</text>
      <text x="292" y="858" text-anchor="middle" fill="#15285a" font-family="Anton, sans-serif" font-size="46" textLength="340" lengthAdjust="spacingAndGlyphs">DORAN PELWICK</text>
    </svg>
  </section>

</div>
</body>
</html>
```